Webshop for furniture and lamps

We need a design for a web shop with APP that should have two options:
1-Webshop in general which should attract to private customer in general and
2-Website that is meant to attract big customers as hotels and restaurants who would have their own customerize login.

That's the idea behind the shop.

It should be diveded into 4 parts
vintage furniture
rattan set outdoor and indoor
lamps and
wooden wall decor

The name of the shop is brisa novelta!

Please kindly make me an offer.

Reason: Dear designers, so far there hasn't been a design that really matched. Look up German web sites like www.fernblick-art.de or www.holzkante17.de... Haven't been convinced by designs! Sorry folks. Please submit some new ones. Kind regards Ned

```html
<!DOCTYPE html>
<html lang="en">
<head>
<meta charset="utf-8">
<title>Brisa Novelta – Vintage Furniture</title>
<link rel="stylesheet" href="https://fonts.googleapis.com/css2?family=Oswald:wght@400&family=Michroma&family=Open+Sans:wght@400&family=Arimo:wght@400&display=swap">
<style>
:root{
  --page:#ffffff;
  --header-bg:#f5f5f5;
  --ink:#2b2b2b;
  --nav-ink:#333333;
  --dark:#3a3b3b;
  --dark-line:#4a4b4b;
  --panel:rgba(40,40,40,.88);
  --side-bg:#f1efdc;
  --line:#7a7a7a;
  --accent:#e8485f;
  --icon-grey:#8d8d8d;
  --gold:#a99870;
  --foot-ink:#bdbdbd;
  --foot-dim:#8e8e8e;
}
*{box-sizing:border-box;margin:0;padding:0}
html,body{width:903px;height:1200px;overflow:hidden}
body{position:relative;background:var(--page);font-family:"Open Sans",sans-serif;color:var(--ink)}
.abs{position:absolute}

/* header */
.site-header{left:0;top:0;width:903px;height:78px;background:var(--header-bg)}
.brand{left:94px;top:26px;font-family:"Michroma",sans-serif;font-size:17px;letter-spacing:4px;color:#222;text-transform:uppercase;white-space:nowrap}
.main-nav{top:29px;font-family:"Oswald",sans-serif;font-size:14px;color:var(--nav-ink)}

/* hero */
.hero{left:0;top:78px;width:903px;height:403px;background:linear-gradient(180deg,#6f6a4e 0%,#57523d 60%,#2c2520 78%,#1c1714 100%)}
.hero-chair{left:390px;top:20px;width:420px;height:383px;background:radial-gradient(ellipse at 50% 45%,#efe6cf 0%,#d9ccb0 45%,rgba(150,140,120,.6) 75%,rgba(0,0,0,0) 100%)}
.hero-panel{left:94px;top:139px;width:321px;height:203px;background:var(--panel);border:1px solid #6a6a6a}
.hero-title{left:25px;top:36px;font-family:"Michroma",sans-serif;font-size:17px;letter-spacing:4px;color:#fff;text-transform:uppercase;white-space:nowrap}
.hero-text{left:26px;top:65px;width:268px;font-size:12.4px;line-height:16.4px;color:#f1f1f1;text-align:justify}
.hero-btn{left:182px;top:134px;width:110px;height:45px;background:#3c3c3c;border:1px solid #777;color:#fff;font-size:16px;line-height:43px;text-align:center}
.hero-arrows{left:96px;top:434px}

/* sidebar */
.side{left:83px;top:497px;width:196px;border:1px solid var(--line)}
.side-head{height:40px;background:#fff;border-bottom:1px solid var(--line);font-family:"Michroma",sans-serif;font-size:15px;letter-spacing:3px;line-height:40px;padding-left:11px;text-transform:uppercase}
.side-item{height:38.4px;background:var(--side-bg);border-bottom:1px solid var(--line);font-size:11.5px;line-height:38px;padding-left:30px;position:relative}
.side-item:last-child{border-bottom:none}
.side-item::before{content:"→";position:absolute;left:14px;font-size:8px}

.crumbs{left:294px;top:499px;font-size:11.5px;color:#333;white-space:nowrap}
.crumbs .sep{margin:0 7px;font-size:10px}

/* product cards */
.card{width:165px;height:186px;border:1px solid var(--line);background:#fff}
.card-img{height:107px}
.card-actions{display:flex;height:33px;border-top:1px solid #ddd;border-bottom:1px solid #bbb;background:#fafafa}
.card-actions span{flex:1;display:flex;align-items:center;justify-content:center;border-right:1px solid #e2e2e2}
.card-actions span:last-child{border-right:none}
.card-title{text-align:center;font-size:14.4px;margin-top:5px}
.card-price{text-align:center;font-size:11px;margin-top:3px}

/* footer */
.foot-band{left:0;top:793px;width:903px;height:407px;background:var(--dark)}
.content-sheet{left:75px;top:793px;width:753px;height:139px;background:var(--page)}
.foot-nav{top:966px;font-family:"Arimo",sans-serif;font-size:11px;color:var(--foot-dim)}
.foot-nav.on{color:#fff}
.rule{left:0;width:903px;height:1px;background:var(--dark-line)}
.foot-head{font-family:"Arimo",sans-serif;font-size:13px;color:#dcdcdc}
.social{top:1068px;width:30px;height:30px;background:#5d5e5e}
.email{left:313px;top:1068px;width:150px;height:30px;background:#4a4b4b;color:#7d7d7d;font-size:10px;line-height:30px;padding-left:13px}
.subscribe{left:463px;top:1068px;width:93px;height:30px;background:var(--gold);color:#fff;font-family:"Arimo",sans-serif;font-size:12px;line-height:30px;text-align:center}
.contact-lines{right:99px;top:1059px;text-align:right;font-family:"Arimo",sans-serif;font-size:10px;line-height:13px;color:var(--foot-dim)}
.copyright{left:0;top:1152px;width:906px;text-align:center;font-size:10px;color:#7a7a7a}
</style>
</head>
<body>

<header class="abs site-header">
  <div class="abs brand">brisa novelta</div>
  <nav>
    <span class="abs main-nav" style="left:484px">Home</span>
    <span class="abs main-nav" style="left:535px">About Us</span>
    <span class="abs main-nav" style="left:603px">Services</span>
    <span class="abs main-nav" style="left:669px">Products</span>
    <span class="abs main-nav" style="left:737px">Contact</span>
  </nav>
</header>

<section class="abs hero">
  <div class="abs hero-chair" role="img" aria-label="Ornate cream tufted armchair with silver carved frame against damask wallpaper and a wooden floor"></div>
  <div class="abs hero-panel">
    <div class="abs hero-title">brisa novelta</div>
    <p class="abs hero-text">Duis aute irure dolor in reprehenderit in voluptate velit esse cillum dolore eu fugiat nulla pariatur. Excepteur sint occaecat cupidatat non proident,</p>
    <div class="abs hero-btn">Learn More</div>
  </div>
  <svg class="abs hero-arrows" width="28" height="18" viewBox="0 0 28 18" aria-label="Slide arrows">
    <polyline points="9,2 2,9 9,16" fill="none" stroke="#fff" stroke-width="1.6"/>
    <polyline points="18,2 25,9 18,16" fill="none" stroke="#fff" stroke-width="1.6"/>
  </svg>
</section>

<div class="abs foot-band"></div>
<div class="abs content-sheet"></div>

<aside class="abs side">
  <div class="side-head">Products</div>
  <div class="side-item">Vintage furniture</div>
  <div class="side-item">Rattan set outdoor and indoor</div>
  <div class="side-item">Lamps</div>
  <div class="side-item">Wooden wall decor</div>
</aside>

<div class="abs crumbs">Home<span class="sep">&gt;&gt;</span>Products<span class="sep">&gt;&gt;</span>Vintage Furniture</div>

<svg width="0" height="0" style="position:absolute">
  <defs>
    <symbol id="i-cart" viewBox="0 0 14 12"><path d="M0 1h2.5l2 7h7l1.5-5H4" fill="none" stroke="#e8485f" stroke-width="1.6"/><circle cx="5.5" cy="10.5" r="1.2" fill="#e8485f"/><circle cx="10.5" cy="10.5" r="1.2" fill="#e8485f"/></symbol>
    <symbol id="i-heart" viewBox="0 0 14 12"><path d="M7 11.5L1.3 5.8A3 3 0 0 1 7 2.3a3 3 0 0 1 5.7 3.5z" fill="#e8485f"/></symbol>
    <symbol id="i-swap" viewBox="0 0 14 12"><path d="M1 4h10M8 1l3 3M13 8H3M6 11L3 8" fill="none" stroke="#8d8d8d" stroke-width="1.8"/></symbol>
    <symbol id="i-more" viewBox="0 0 14 14"><circle cx="7" cy="7" r="6" fill="none" stroke="#8d8d8d" stroke-width="1.2"/><polyline points="6,4.5 8.5,7 6,9.5" fill="none" stroke="#8d8d8d" stroke-width="1.2"/></symbol>
  </defs>
</svg>

<!-- product grid -->
<div class="abs card" style="left:295px;top:533px">
  <div class="card-img" role="img" aria-label="Distressed painted wooden side table" style="background:linear-gradient(160deg,#8b6a4d,#b67a62 45%,#6a8c91)"></div>
  <div class="card-actions"><span><svg width="13" height="11"><use href="#i-cart"/></svg></span><span><svg width="13" height="11"><use href="#i-heart"/></svg></span><span><svg width="13" height="11"><use href="#i-swap"/></svg></span><span><svg width="12" height="12"><use href="#i-more"/></svg></span></div>
  <div class="card-title">Product Title</div><div class="card-price">$70 ( 40% Off )</div>
</div>
<div class="abs card" style="left:474px;top:533px">
  <div class="card-img" role="img" aria-label="Vintage wooden cabinet with painted floral tiles" style="background:linear-gradient(160deg,#6b4a34,#9a6a44 50%,#4b3526)"></div>
  <div class="card-actions"><span><svg width="13" height="11"><use href="#i-cart"/></svg></span><span><svg width="13" height="11"><use href="#i-heart"/></svg></span><span><svg width="13" height="11"><use href="#i-swap"/></svg></span><span><svg width="12" height="12"><use href="#i-more"/></svg></span></div>
  <div class="card-title">Product Title</div><div class="card-price">$70 ( 40% Off )</div>
</div>
<div class="abs card" style="left:651px;top:533px">
  <div class="card-img" role="img" aria-label="Painted reclaimed wood table top" style="background:linear-gradient(160deg,#c9c6c0,#8fa6a0 45%,#a8574c 70%,#5b4232)"></div>
  <div class="card-actions"><span><svg width="13" height="11"><use href="#i-cart"/></svg></span><span><svg width="13" height="11"><use href="#i-heart"/></svg></span><span><svg width="13" height="11"><use href="#i-swap"/></svg></span><span><svg width="12" height="12"><use href="#i-more"/></svg></span></div>
  <div class="card-title">Product Title</div><div class="card-price">$70 ( 40% Off )</div>
</div>
<div class="abs card" style="left:295px;top:729px">
  <div class="card-img" role="img" aria-label="Round rattan dining set with stowed chairs" style="background:linear-gradient(180deg,#f2f2f2,#6a6765 45%,#4a4745 80%,#f2f2f2)"></div>
  <div class="card-actions"><span><svg width="13" height="11"><use href="#i-cart"/></svg></span><span><svg width="13" height="11"><use href="#i-heart"/></svg></span><span><svg width="13" height="11"><use href="#i-swap"/></svg></span><span><svg width="12" height="12"><use href="#i-more"/></svg></span></div>
  <div class="card-title">Product Title</div><div class="card-price">$70 ( 40% Off )</div>
</div>
<div class="abs card" style="left:474px;top:729px">
  <div class="card-img" role="img" aria-label="Black rattan outdoor dining set with glass table on a deck" style="background:linear-gradient(180deg,#8a6a52,#2a2e33 45%,#1f2226 80%,#6e5a48)"></div>
  <div class="card-actions"><span><svg width="13" height="11"><use href="#i-cart"/></svg></span><span><svg width="13" height="11"><use href="#i-heart"/></svg></span><span><svg width="13" height="11"><use href="#i-swap"/></svg></span><span><svg width="12" height="12"><use href="#i-more"/></svg></span></div>
  <div class="card-title">Product Title</div><div class="card-price">$70 ( 40% Off )</div>
</div>
<div class="abs card" style="left:651px;top:729px">
  <div class="card-img" role="img" aria-label="Rattan lounge set in a garden" style="background:linear-gradient(180deg,#d9e0e6,#6f8a4f 40%,#8c7a60 70%,#9a9180)"></div>
  <div class="card-actions"><span><svg width="13" height="11"><use href="#i-cart"/></svg></span><span><svg width="13" height="11"><use href="#i-heart"/></svg></span><span><svg width="13" height="11"><use href="#i-swap"/></svg></span><span><svg width="12" height="12"><use href="#i-more"/></svg></span></div>
  <div class="card-title">Product Title</div><div class="card-price">$70 ( 40% Off )</div>
</div>

<footer>
  <span class="abs foot-nav on" style="left:248px">Home</span>
  <span class="abs foot-nav" style="left:326px">About us</span>
  <span class="abs foot-nav" style="left:418px">Services</span>
  <span class="abs foot-nav" style="left:509px">Products</span>
  <span class="abs foot-nav" style="left:601px">Contact Us</span>
  <div class="abs rule" style="top:1011px"></div>

  <div class="abs foot-head" style="left:87px;top:1036px">Follow Us</div>
  <div class="abs social" style="left:86px" role="img" aria-label="Social network link"></div>
  <div class="abs social" style="left:122px" role="img" aria-label="Social network link"></div>
  <div class="abs social" style="left:160px" role="img" aria-label="Social network link"></div>

  <div class="abs foot-head" style="left:316px;top:1038px">News letter</div>
  <div class="abs email">Enter your email</div>
  <div class="abs subscribe">Subscribe</div>

  <div class="abs foot-head" style="right:101px;top:1035px">Contact Us</div>
  <div class="abs contact-lines">Address<br>New Street<br>ph :xxxxx-xxx-xxx</div>

  <div class="abs rule" style="top:1130px"></div>
  <div class="abs copyright">Lumen Yard © 2014 Allright Reserved</div>
</footer>

</body>
</html>
```